Business Card for By Karel Voss

Looking to have a business card designed for my lifestyle and fitness company. My company offers personal training, online programming and nutrition advice based out of London, United Kingdom.

I'd like to see modern, sleek designs, focusing on black, matte black or matte grey. Design doesn't need to be overly descriptive as this will also be used as a personal business card. I've included my logo.

Please note that my company is no longer called "Fitness by Karel Voss" but instead "By Karel Voss", this is because of my other ventures. Therefore please don't use the "fitness by karel voss" text.

information about my company can be found at www.bykarelvoss.com

Company is also based out of London (United Kingdom) & Sydney (Australia) this could be reflected on the card.

Industry/Entity Type

Business

Contact Information for Business Card

Karel Voss
+44 7382 615027
karel@bykarelvoss.com
www.bykarelvoss.com

Font styles to use
Sans Serif

Requirements
Must have
• All contact details and inclusion of my logo.

```html
<!DOCTYPE html>
<html lang="en">
<head>
<meta charset="utf-8">
<title>Karel Voss — Business Card</title>
<link href="https://fonts.googleapis.com/css2?family=Roboto+Condensed:wght@400;700&display=swap" rel="stylesheet">
<style>
  :root {
    --backdrop: #161a19;
    --card: #dcdcdc;
    --ink: #111111;
    --ink-soft: #2a2a2a;
  }
  html, body {
    margin: 0;
    padding: 0;
    width: 1200px;
    height: 1200px;
    overflow: hidden;
    background: var(--backdrop);
    font-family: "Roboto Condensed", sans-serif;
  }
  .card {
    position: absolute;
    left: 150px;
    width: 840px;
    background: var(--card);
    color: var(--ink);
  }
  .card--front { top: 87px; height: 480px; }
  .card--back { top: 600px; height: 484px; }

  .rule {
    position: absolute;
    height: 3px;
    background: var(--ink);
  }

  .brand {
    position: absolute;
    text-align: center;
    font-weight: 700;
    text-transform: uppercase;
    letter-spacing: 4px;
    line-height: 1.05;
    color: var(--ink);
  }
  .brand--front { left: 274px; width: 292px; top: 222px; font-size: 27px; }
  .brand--back { left: 55px; width: 228px; top: 203px; font-size: 23px; letter-spacing: 3px; }

  .brand-mark {
    position: absolute;
    border-radius: 50%;
    background: var(--ink);
  }

  .web-line {
    position: absolute;
    left: 278px;
    top: 412px;
    display: flex;
    align-items: center;
    gap: 8px;
    font-size: 21px;
    color: var(--ink-soft);
  }

  .identity {
    position: absolute;
    right: 78px;
    top: 140px;
    text-align: right;
  }
  .identity-name {
    margin: 0;
    font-size: 42px;
    font-weight: 400;
    line-height: 1;
  }
  .identity-title {
    margin: 4px 0 0;
    font-size: 21px;
    line-height: 1;
  }
  .contact-list {
    position: absolute;
    right: 80px;
    top: 256px;
    margin: 0;
    padding: 0;
    list-style: none;
    text-align: right;
    font-size: 20px;
    color: var(--ink-soft);
  }
  .contact-list li { height: 37.5px; }
</style>
</head>
<body>

<section class="card card--front">
  <div class="brand-mark" style="left:372px; top:93px; width:96px; height:96px;"></div>
  <div class="rule" style="left:0; width:274px; top:235px;"></div>
  <div class="rule" style="left:566px; width:274px; top:235px;"></div>
  <div class="brand brand--front">By<br>Karel Voss</div>
  <div class="web-line">
    <svg width="36" height="36" viewBox="0 0 36 36" aria-hidden="true">
      <g fill="none" stroke="#111" stroke-width="1.6">
        <circle cx="18" cy="18" r="15"/>
        <ellipse cx="18" cy="18" rx="7" ry="15"/>
        <line x1="3" y1="18" x2="33" y2="18"/>
        <line x1="18" y1="3" x2="18" y2="33"/>
        <path d="M6 10 H30 M6 26 H30"/>
      </g>
    </svg>
    <span>www.bykarelvoss.com</span>
  </div>
</section>

<section class="card card--back">
  <div class="brand-mark" style="left:130px; top:94px; width:80px; height:80px;"></div>
  <div class="rule" style="left:0; width:55px; top:215px;"></div>
  <div class="rule" style="left:283px; width:479px; top:215px;"></div>
  <div class="rule" style="left:784px; width:56px; top:215px;"></div>
  <div class="brand brand--back">By<br>Karel Voss</div>

  <div class="identity">
    <h1 class="identity-name">Karel Voss</h1>
    <p class="identity-title">Your Title</p>
  </div>
  <ul class="contact-list">
    <li>+44 7382 615027</li>
    <li>karel@bykarelvoss.com</li>
    <li>www.bykarelvoss.com</li>
  </ul>
</section>

</body>
</html>
```